Card Show Flyer- for use on instagram, facebook and twitter

My usual digital flyer designer isnt getting back to me. I need something that looks like the image that I am uploading with a new design for our next show.
Dellmoor Trading Jamboree-Memorial Day Show
742 N. Halvard Lane
Corvalle Indiana 47812
Monday, May 29th-Show- 8:30-3:30
Sunday, May 28th-Trade Night- 6pm-10pm
180+ Sold Out Tables
Notes
-use trade night sponsored by Gripline Kiosks
-use pavrin top banner like the copy i am submitting
-use tumbleweed logo at bottom with "Best Kids Card Scavenger Hunt in the Midwest"
-use QVR logo with "official group grading submitter for Dellmoor Trading Jamboree"
Attaching our Orlo Athletics logo as well for your use where needed
Thanks! Gary Tolliver

Target Market(s)

Collectors, Attendance for card show

Industry/Entity Type

Collectibles/Trade Show

Requirements
Must have
• My logo and specifics for partnerships

```html
<!DOCTYPE html>
<html lang="en">
<head>
<meta charset="utf-8">
<title>Dellmoor Trading Jamboree – Memorial Day Show</title>
<link rel="stylesheet" href="https://fonts.googleapis.com/css2?family=Alfa+Slab+One&family=Barlow+Condensed:wght@600;700&family=Barlow+Semi+Condensed:wght@500;600;700&display=swap">
<style>
  :root {
    --stage: #eeeeee;
    --royal: #0b4fb0;
    --navy: #0c1f4a;
    --orange: #f0531c;
    --yellow: #f3e21b;
    --white: #ffffff;
    --steel: #3f4048;
    --link-blue: #2f6fcf;
    --partner-grey: #8a8a8e;
    --title-font: "Barlow Condensed", sans-serif;
    --slab-font: "Alfa Slab One", serif;
    --body-font: "Barlow Semi Condensed", sans-serif;
  }
  * { margin: 0; padding: 0; box-sizing: border-box; }
  html, body { width: 1200px; height: 1177px; overflow: hidden; background: var(--stage); }
  .flyer {
    position: absolute; left: 154px; top: 110px;
    width: 754px; height: 795px;
    transform: scale(1.2); transform-origin: 0 0;
    background: var(--royal); overflow: hidden;
    font-family: var(--body-font); color: var(--white);
    box-shadow: 0 2px 8px rgba(0,0,0,.25);
  }
  .flyer-shapes { position: absolute; inset: 0; width: 754px; height: 795px; }
  .abs { position: absolute; }

  .event-title {
    left: 24px; top: 16px;
    font-family: var(--title-font); font-weight: 700;
    font-size: 62px; line-height: .93; letter-spacing: .5px;
    background: linear-gradient(180deg, #ffffff 45%, #b9bcc4 100%);
    -webkit-background-clip: text; background-clip: text; color: transparent;
  }
  .show-banner {
    left: 24px; top: 222px; width: 440px; text-align: center;
    font-family: var(--slab-font); font-size: 30px; letter-spacing: .5px;
    background: linear-gradient(180deg, #ffffff 50%, #aeb2bb 100%);
    -webkit-background-clip: text; background-clip: text; color: transparent;
  }

  .day { text-align: center; }
  .day-name { font-size: 19px; font-weight: 500; line-height: 1; }
  .day-date { font-family: var(--slab-font); font-size: 25px; line-height: 1.1; margin-top: 3px; }
  .day-time { font-size: 18px; font-weight: 500; line-height: 1.1; }
  .day-label { font-family: var(--title-font); font-weight: 700; line-height: .9; text-align: center; }

  .trade-night { left: 52px; top: 330px; width: 238px; }
  .trade-night .day-date .num { color: var(--orange); }
  .trade-night-label { left: 52px; top: 428px; width: 238px; color: var(--orange); font-size: 42px; }

  .show-day { left: 264px; top: 452px; width: 266px; }
  .show-day .day-date .num { color: var(--yellow); }
  .show-day-label { left: 264px; top: 562px; width: 266px; color: var(--yellow); font-size: 46px; }

  .table-count {
    left: 310px; top: 312px; width: 176px; text-align: center;
    font-size: 27px; font-weight: 600; line-height: 1.05;
  }

  .sponsor { left: 70px; top: 556px; width: 200px; text-align: center; color: var(--navy); }
  .sponsor-label { font-size: 12px; font-weight: 600; line-height: 1.1; color: var(--steel); }
  .sponsor-name {
    display: inline-flex; align-items: center; gap: 6px; margin-top: 14px;
    font-size: 17px; font-weight: 700; color: var(--navy);
  }
  .sponsor-name .mark { width: 14px; height: 14px; background: var(--navy); }

  .badge-name {
    left: 530px; top: 70px; width: 184px; text-align: center;
    font-size: 24px; font-weight: 700; line-height: 1.05; color: var(--white);
  }

  .venue {
    left: 614px; top: 336px; width: 140px; text-align: center; font-style: normal;
    font-size: 17px; font-weight: 600; line-height: 1.12;
  }

  .partner-box {
    display: flex; align-items: center; justify-content: center;
    font-size: 17px; font-weight: 700;
  }
  .tumbleweed-box { left: 617px; top: 488px; width: 107px; height: 106px; background: var(--partner-grey); color: var(--white); }
  .qvr-box { left: 624px; top: 660px; width: 98px; height: 106px; background: var(--navy); color: var(--white); font-size: 24px; }
  .partner-note { font-size: 13px; font-weight: 700; line-height: 1.3; color: var(--navy); text-transform: uppercase; text-align: center; }
  .hunt-note { left: 606px; top: 602px; width: 128px; }
  .grading-note { left: 494px; top: 683px; width: 122px; }

  .contact { left: 0; top: 668px; width: 330px; height: 127px; }
  .contact-name { position: absolute; left: 56px; top: 4px; font-family: var(--slab-font); font-size: 17px; color: var(--yellow); }
  .contact-line { position: absolute; left: 34px; display: flex; align-items: center; gap: 8px; font-size: 15px; font-weight: 600; line-height: 1; }
  .contact-line .icon { width: 14px; height: 14px; flex: none; }
  .contact-line .dot { width: 12px; height: 12px; background: var(--link-blue); flex: none; margin: 0 1px; }
  .contact-email { top: 32px; }
  .contact-dm { top: 52px; left: 56px; font-family: var(--slab-font); font-size: 13px; font-weight: 400; color: var(--link-blue); }
  .contact-fb { top: 73px; }
  .contact-ig { top: 94px; }
</style>
</head>
<body>
<main class="flyer">
  <svg class="flyer-shapes" viewBox="0 0 754 795" aria-hidden="true">
    <polygon points="445,0 754,0 754,293 612,293 540,370 470,236 510,200" fill="var(--navy)"/>
    <polygon points="0,206 470,206 490,215 0,215" fill="var(--orange)"/>
    <polygon points="0,218 470,218 500,243 470,268 0,268" fill="var(--navy)" stroke="var(--orange)" stroke-width="4"/>
    <rect x="612" y="293" width="142" height="135" fill="var(--orange)"/>
    <polygon points="645,293 691,293 668,318" fill="var(--navy)"/>
    <path d="M668 276c-7 0-12 5-12 12 0 9 12 22 12 22s12-13 12-22c0-7-5-12-12-12zm0 16a4 4 0 1 1 0-8 4 4 0 0 1 0 8z" fill="var(--yellow)"/>
    <polygon points="540,428 754,428 754,795 402,795" fill="var(--white)"/>
    <polygon points="312,653 326,653 404,795 390,795" fill="var(--orange)"/>
    <polygon points="0,668 285,668 322,795 0,795" fill="var(--navy)"/>
    <polygon points="52,408 107,296 237,296 290,408 237,520 107,520" fill="var(--navy)" stroke="var(--orange)" stroke-width="6"/>
    <line x1="80" y1="414" x2="262" y2="414" stroke="var(--royal)" stroke-width="2"/>
    <polygon points="57,598 85,543 250,543 272,598 250,653 85,653" fill="var(--white)"/>
    <polygon points="264,535 318,423 476,423 530,535 476,647 318,647" fill="var(--navy)" stroke="var(--yellow)" stroke-width="6"/>
    <line x1="292" y1="536" x2="502" y2="536" stroke="var(--royal)" stroke-width="2"/>
    <circle cx="622" cy="108" r="100" fill="var(--white)"/>
    <circle cx="622" cy="108" r="94" fill="var(--link-blue)"/>
    <circle cx="622" cy="108" r="70" fill="var(--navy)"/>
  </svg>

  <h1 class="abs event-title">DELLMOOR<br>TRADING<br>JAMBOREE</h1>
  <h2 class="abs show-banner">MEMORIAL DAY SHOW</h2>

  <div class="abs badge-name">Dellmoor Trading Jamboree</div>

  <section class="abs day trade-night">
    <p class="day-name">SUNDAY</p>
    <p class="day-date">MAY <span class="num">28</span>TH</p>
    <p class="day-time">6pm-10pm</p>
  </section>
  <p class="abs day-label trade-night-label">TRADE<br>NIGHT</p>

  <p class="abs table-count">180+<br>SOLD OUT<br>TABLES</p>

  <section class="abs day show-day">
    <p class="day-name">MONDAY</p>
    <p class="day-date">MAY <span class="num">29</span>TH</p>
    <p class="day-time">8:30am-3.30pm</p>
  </section>
  <p class="abs day-label show-day-label">SHOW</p>

  <div class="abs sponsor">
    <p class="sponsor-label">TRADE NIGHT<br>SPONSORED BY</p>
    <p class="sponsor-name"><span class="mark"></span>Gripline Kiosks</p>
  </div>

  <address class="abs venue">742 N.<br>Halvard Lane<br>Corvalle<br>Indiana 47812</address>

  <div class="abs partner-box tumbleweed-box">tumbleweed</div>
  <p class="abs partner-note hunt-note">"Best kids card<br>scavenger hunt<br>in the Midwest</p>

  <p class="abs partner-note grading-note">Official group<br>grading<br>submitter for<br>Dellmoor<br>Trading Jamboree</p>
  <div class="abs partner-box qvr-box">QVR</div>

  <section class="abs contact">
    <p class="contact-name">GARY TOLLIVER</p>
    <p class="contact-line contact-email">
      <svg class="icon" viewBox="0 0 14 14" aria-hidden="true"><rect x="1" y="3" width="12" height="9" fill="var(--link-blue)"/><path d="M1 3l6 5 6-5" stroke="var(--navy)" stroke-width="1.4" fill="none"/></svg>
      gtolliver@dellmoormail.com
    </p>
    <p class="contact-line contact-dm">OR DIRECT MESSAGE VIA</p>
    <p class="contact-line contact-fb"><span class="dot"></span>the dellmoorjamboree</p>
    <p class="contact-line contact-ig"><span class="dot"></span>orlo_athletics</p>
  </section>
</main>
</body>
</html>
```